Business Card Design

BrightHarbor is a fund management company that takes just four market positions a year. each position is linked to a big geopolitical and economic event happening in the world. So for example we may be buying gold mining stocks-these are the companies who dig the gold out of the ground, as all the gold is currently being bought by Asia, or buying the japanese stock market as this is one of the big stories of today.

I am looking for a logo that represents 'BrightHarbor'-the Bright Harbor.

I would like it to be small and sit to the left of the name of the company on the left hand side(I think!)on the top line of the business card please.

Industry/Entity Type

Mining

Contact Information for Business Card

BrightHarbor Capital management Ltd
41 Pellam Street
London E9T 2QN

Martin J Colby

Mob: 0(44)7823946250
Off: 0(44) 207 xxxx
email: mc@brightharbor-cm.example

```html
<!DOCTYPE html>
<html lang="en">
<head>
<meta charset="utf-8">
<title>BrightHarbor Business Card</title>
<link rel="stylesheet" href="https://fonts.googleapis.com/css2?family=Tinos&display=swap">
<style>
  :root {
    --card-bg: #ffffff;
    --brand-blue: #3b94ee;
    --mark-blue: #2f6fb8;
  }
  html, body {
    margin: 0;
    padding: 0;
    width: 1200px;
    height: 702px;
    overflow: hidden;
    background: var(--card-bg);
  }
  .card {
    position: relative;
    width: 1200px;
    height: 702px;
    background: var(--card-bg);
    font-family: "Tinos", "Times New Roman", serif;
    color: var(--brand-blue);
  }
  .brand-mark {
    position: absolute;
    left: 104px;
    top: 77px;
  }
  .brand-name {
    position: absolute;
    left: 257px;
    width: 600px;
    top: 236px;
    margin: 0;
    text-align: center;
    font-size: 76px;
    font-weight: 400;
    font-variant: small-caps;
    letter-spacing: 1px;
    line-height: 1;
    color: var(--brand-blue);
  }
  .address {
    position: absolute;
    left: 81px;
    top: 472px;
    margin: 0;
    font-style: normal;
    font-size: 42px;
    line-height: 1;
  }
  .address-line {
    display: block;
    height: 56px;
  }
  .address-line--postcode {
    padding-left: 10px;
    margin-top: 6px;
  }
</style>
</head>
<body>
  <main class="card">
    <svg class="brand-mark" width="104" height="122" viewBox="0 0 104 122" aria-hidden="true">
      <ellipse cx="52" cy="61" rx="51" ry="60" fill="var(--mark-blue)"/>
    </svg>

    <h1 class="brand-name">BrightHarbor</h1>

    <address class="address">
      <span class="address-line">BrightHarbor Capital Management L.T.D</span>
      <span class="address-line">41 Pellam Street London</span>
      <span class="address-line address-line--postcode">E9T 2QN</span>
    </address>
  </main>
</body>
</html>
```